ClipNestra.com - Landing Page

I need a Landing Page to present ClipNestra.com. It is a Platform that will allow people to COLLABORATE to produce Video Projects (Movies, Documentaries, Tv Shows etc).

As I described in the comments AT THE BEGINNING there will be just one Social Movie (is how we call a Video Project) featured in the Landing Page and others will follow.

In the Landing Page I need just the BASIC features of a WebSite to keep contact with who is interested in the Project (email contact etc).
Updates

Project Deadline Extended
Reason: Dears in the last few days several designers showed interest in submitting a Design for this project. I think is better if I give few days more for them to prepare their submissions. So I extended the deadline for 7 days Thanks Tomas

Target Market(s)

Wannabe Video Directors/ Producers around the world

Industry/Entity Type

Movie

Requirements
Must have
• a) Designed to be ready for Responsive Web Design.

b) Landing Page with possible infinite Scrolling

c) At the Centre of the Page there must the Space for to embed an image that is a link to another WebSite that is under construction. This other WebSite is the first Experiment of a Collaborative Video Production over the Web

d) Even if the ClipNestra Logo is in Black and White (see below 2 versions) there is no need that the Site is in Black and White. The colors fit the Logo
Should not have
• a) Parallax

```html
<!DOCTYPE html>
<html lang="en">
<head>
<meta charset="utf-8">
<title>ClipNestra – Landing Page</title>
<link rel="stylesheet" href="https://fonts.googleapis.com/css2?family=PT+Sans+Narrow:wght@400;700&family=Open+Sans:ital,wght@0,400;0,600;0,700;1,400&display=swap">
<style>
:root{
  --bg-dark:#1a1a1a;
  --bg-wood:#242424;
  --panel:#262626;
  --panel-line:#4a4a4a;
  --footer:#0a0a0a;
  --text:#d6d6d6;
  --text-dim:#a9a9a9;
  --white:#ffffff;
  --orange-top:#ffb21a;
  --orange-bot:#f08a00;
  --btn-dark:#0d0d0d;
  --field:#f4f4f4;
  --sky-top:#5f8fc4;
  --sky-bot:#c9a88e;
}
*{margin:0;padding:0;box-sizing:border-box}
html,body{width:959px;height:1200px;overflow:hidden}
body{
  position:relative;
  background:linear-gradient(90deg,#161616 0%,var(--bg-wood) 30%,#202020 60%,#151515 100%);
  font-family:"Open Sans",sans-serif;color:var(--text);
}
.abs{position:absolute}
.heading{font-family:"PT Sans Narrow",sans-serif;color:var(--white);text-transform:uppercase;font-weight:400}

/* header */
.brand-mark{left:112px;top:22px;width:92px;height:92px;border:2px solid #e8e8e8;border-radius:50%}
.brand-name{left:222px;top:44px;font-family:"Open Sans",sans-serif;font-size:28px;font-weight:400;color:#eeeeee}
.auth-btn{top:4px;height:26px;background:linear-gradient(#ffffff,#d8d8d8);color:#222;font-family:"PT Sans Narrow",sans-serif;font-size:13px;text-align:center;line-height:26px;text-transform:uppercase}
.search{left:630px;top:46px;width:224px;height:26px;border-radius:5px;background:linear-gradient(#3b3b3b,#2b2b2b);border:1px solid #444}
.search span{position:absolute;left:20px;top:6px;font-size:9px;color:#9a9a9a}
.search-btn{position:absolute;right:4px;top:4px;width:17px;height:16px;background:#777;border-radius:2px}
.nav a{position:absolute;top:106px;font-family:"PT Sans Narrow",sans-serif;font-size:15px;color:#e2e2e2;text-decoration:none;text-transform:uppercase}
.nav-active{left:522px;top:82px;width:66px;height:50px;background:#0d0d0d;border-radius:4px 4px 0 0;border:1px solid #333;border-bottom:none}
.nav-sep{top:104px;width:1px;height:24px;background:#555}

/* hero */
.film-deco{background:linear-gradient(160deg,rgba(200,200,200,.35),rgba(120,120,120,.15));border-radius:8px}
.hero-frame{left:88px;top:130px;width:770px;height:287px;background:#2e3138;border:1px solid #3f434b}
.hero-photo{left:96px;top:140px;width:753px;height:266px;background:linear-gradient(180deg,var(--sky-top) 0%,#7aa1c9 55%,var(--sky-bot) 100%)}
.hero-title{left:559px;top:212px;font-size:17px;width:270px;border-bottom:1px solid rgba(255,255,255,.5);padding-bottom:4px}
.hero-text{left:559px;top:242px;width:278px;font-size:9.3px;line-height:16.8px;color:var(--white)}
.btn-orange{background:linear-gradient(var(--orange-top),var(--orange-bot));color:var(--white);font-family:"PT Sans Narrow",sans-serif;font-weight:700;text-align:center;border-radius:3px}
.hero-cta{left:558px;top:338px;width:124px;height:38px;line-height:38px;font-size:19px}
.pager{left:414px;top:404px;width:144px;height:24px;background:linear-gradient(#f2f2f2,#cfd3d9);border-radius:3px;border:1px solid #9aa}
.pager i{position:absolute;top:9px;width:7px;height:7px;border-radius:50%;background:#8a8f96}
.pager i.on{background:#111}

/* main panel */
.main-panel{left:86px;top:452px;width:772px;height:604px;border:1px solid var(--panel-line);background:rgba(30,30,30,.55)}
.section-title{font-size:18px}
.lead{left:105px;top:499px;font-size:9.6px;font-weight:700;color:var(--white)}
.body-text{font-size:8.7px;line-height:14.4px;color:var(--text)}
.btn-dark{background:linear-gradient(#2a2a2a,var(--btn-dark));color:var(--white);font-family:"PT Sans Narrow",sans-serif;font-weight:700;text-align:center}
.projects-bar{left:106px;top:676px;width:454px;height:30px;background:#1c1c1c}
.project{left:109px;width:450px;height:90px}
.project .thumb{position:absolute;left:0;top:0;width:153px;height:88px;border:2px solid #777}
.project .play{position:absolute;left:65px;top:32px;width:22px;height:22px;border-radius:50%;background:rgba(220,220,220,.7)}
.project .play:after{content:"";position:absolute;left:8px;top:6px;border-left:8px solid #333;border-top:5px solid transparent;border-bottom:5px solid transparent}
.project h3{position:absolute;left:165px;top:6px;font-family:"PT Sans Narrow",sans-serif;font-weight:400;font-size:13.5px;color:var(--white)}
.project .author{position:absolute;left:165px;top:26px;font-size:8.5px;color:var(--text)}
.project .desc{position:absolute;left:165px;top:38px;width:290px;font-size:8.5px;line-height:13px;color:var(--text)}
.project .more{position:absolute;left:167px;top:65px;width:54px;height:24px;line-height:24px;font-size:9.5px;background:#0c0c0c;color:var(--white);text-align:center;border-radius:2px}
.share{position:absolute;top:70px;height:15px;display:flex;gap:2px}
.share b{font-weight:600;font-size:8.5px;background:#eef0f4;color:#2d4a82;padding:0 4px;line-height:15px;border-radius:2px}
.share em{font-style:normal;font-size:8px;background:#fff;color:#333;padding:0 3px;line-height:15px;border:1px solid #ccc}

.video{left:603px;top:501px;width:220px;height:124px;border:2px solid #555;background:linear-gradient(180deg,#7f9cc0 0%,#b9c7d6 55%,#4a3d3a 100%)}
.video-bar{left:605px;top:613px;width:216px;height:10px;background:#111}
.video-bar i{position:absolute;left:0;top:0;width:50px;height:2px;background:#d11}
.video-play{left:700px;top:547px;width:26px;height:18px;background:rgba(0,0,0,.8);border-radius:3px}
.video-play:after{content:"";position:absolute;left:10px;top:4px;border-left:8px solid #fff;border-top:5px solid transparent;border-bottom:5px solid transparent}

.contact-box{left:608px;top:728px;width:214px;height:272px;border-radius:12px;background:linear-gradient(#3a3a3a,#2a2a2a);border:2px solid #555}
.contact-icon{left:620px;top:738px;width:30px;height:24px;background:#f2f2f2;border-radius:3px}
.field{left:626px;width:177px;height:25px;background:var(--field);border:1px solid #bbb;font-size:8.5px;font-style:italic;color:#777;padding:6px 12px}
.submit{left:710px;top:961px;width:92px;height:33px;line-height:33px;font-size:13px;font-style:italic}

/* footer */
.footer{left:0;top:1068px;width:959px;height:132px;background:var(--footer)}
.footer-title{left:82px;top:1087px;font-family:"PT Sans Narrow",sans-serif;font-size:17px;color:var(--white)}
.footer-text{left:82px;top:1117px;width:220px;font-size:8.5px;line-height:14px;color:#cfcfcf}
.email-input{left:85px;top:1154px;width:188px;height:23px;background:#fff;font-size:8px;font-style:italic;color:#999;padding:6px 10px}
.subscribe{left:283px;top:1157px;width:68px;height:23px;line-height:23px;font-size:10px;background:#222;color:#fff;font-weight:600;text-align:center;border-radius:2px}
.footer-links a{position:absolute;font-size:8.8px;color:#cfcfcf;text-decoration:none}
.footer-links a:before{content:"›";margin-right:7px;color:#888}
.social{top:1091px;width:22px;height:22px;border-radius:2px}
.copyright{right:105px;top:1133px;font-size:8.8px;color:#cfcfcf;text-align:right;line-height:15px}
</style>
</head>
<body>

<!-- header -->
<div class="abs brand-mark"></div>
<div class="abs brand-name">ClipNestra</div>
<div class="abs auth-btn" style="left:726px;width:60px">Login</div>
<div class="abs auth-btn" style="left:791px;width:60px">Register</div>
<div class="abs search"><span>Search</span><div class="search-btn"></div></div>

<nav class="nav">
  <div class="abs nav-active"></div>
  <a style="left:542px">Home</a>
  <a style="left:608px">Collaborate</a>
  <div class="abs nav-sep" style="left:689px"></div>
  <a style="left:710px">About Us</a>
  <div class="abs nav-sep" style="left:774px"></div>
  <a style="left:795px">Contact Us</a>
</nav>

<!-- hero -->
<div class="abs film-deco" role="img" aria-label="Curling film strip decoration" style="left:0;top:136px;width:88px;height:200px"></div>
<div class="abs film-deco" role="img" aria-label="Curling film strip decoration" style="left:858px;top:136px;width:101px;height:184px"></div>
<div class="abs hero-frame"></div>
<div class="abs hero-photo" role="img" aria-label="Camera operator silhouetted against a blue sky, filming an interview on the camera screen"></div>
<h1 class="abs heading hero-title">Lorem ipsum dolor sit amet, elit</h1>
<p class="abs hero-text">Cum sociis natoque penatibus et magnis dis parturient montes, nascetur ridiculus mus. In iaculis facilisis massa. Etiam eu urna. Sed porta.Cum sociis natoque penatibus et magnis dis parturient montes, nascetur ridiculus mus. In iaculis facilisis massa. Etiam eu urna. Sed porta.</p>
<div class="abs btn-orange hero-cta">SIGN UP</div>
<div class="abs pager">
  <i style="left:28px"></i><i style="left:43px"></i><i class="on" style="left:58px"></i><i style="left:72px"></i><i style="left:87px"></i><i style="left:101px"></i>
</div>

<!-- main -->
<div class="abs main-panel"></div>
<h2 class="abs heading section-title" style="left:105px;top:470px">Welcome to ClipNestra</h2>
<p class="abs lead">Mauris vel lacus vitae felis vestibulum volutpat. Etiam est nunc, venisl.</p>
<p class="abs body-text" style="left:106px;top:520px;width:456px">Sed ut perspiciatis unde omnis iste natus error sit voluptatem accusantium doloremque laudantium, totam rem aperiam, eaque ipsa quae ab illo inventore veritatis et quasi architecto beatae vitae dicta sunt explicabo. Nemo enim ipsam voluptatem quia voluptas sit aspernatur aut odit aut fugit, sed quia consequuntur magni dolores eos qui ratione voluptatem sequi nesciunt. Neque porro quisquam est, qui dolorem ipsum quia dolor sit amet.Sed ut perspiciatis unde omnis iste natus error sit voluptatem accusantium doloremque laudantium, totam rem aperiam, eaque ipsa quae ab illo inventore veritatis et quasi architecto beatae vitae dicta sunt explicabo. Nemo enim ipsam voluptatem quia voluptas</p>
<div class="abs btn-dark" style="left:490px;top:624px;width:64px;height:26px;line-height:26px;font-size:12px">More</div>

<div class="abs projects-bar"></div>
<h2 class="abs heading section-title" style="left:116px;top:681px">Video Projects</h2>

<div class="abs project" style="top:718px">
  <div class="thumb" role="img" aria-label="Video still of riders on a racing track" style="background:linear-gradient(135deg,#6f7a86,#c9b36a,#5a5f66)"><div class="play"></div></div>
  <h3>Sed ut perspiciatis unde omnis iste natus</h3>
  <div class="author">Author: Dana Whitlow</div>
  <div class="desc">Sed ut perspiciatis unde omnis iste natus error sit voluptatem accus-antium doloremque laudantium, totam rem aperiam, ipsa quae.</div>
  <div class="more">More &gt;&gt;</div>
  <div class="share" style="left:252px"><b>Like</b><em>20</em></div>
  <div class="share" style="left:308px"><b>Share</b><em>20</em></div>
  <div class="share" style="left:387px"><b>+1</b><em>20</em></div>
</div>

<div class="abs project" style="top:831px">
  <div class="thumb" role="img" aria-label="Underwater video still of a coral reef with fish" style="background:linear-gradient(160deg,#3a8fb8,#1d5f7e,#2a4a55)"><div class="play"></div></div>
  <h3>Sed ut perspiciatis unde omnis iste natus</h3>
  <div class="author">Author: Dana Whitlow</div>
  <div class="desc">Sed ut perspiciatis unde omnis iste natus error sit voluptatem accus-antium doloremque laudantium, totam rem aperiam, ipsa quae.</div>
  <div class="more">More &gt;&gt;</div>
  <div class="share" style="left:252px"><b>Like</b><em>20</em></div>
  <div class="share" style="left:308px"><b>Share</b><em>20</em></div>
  <div class="share" style="left:387px"><b>+1</b><em>20</em></div>
</div>

<div class="abs project" style="top:944px">
  <div class="thumb" role="img" aria-label="Video still of a group of performers on stage" style="background:linear-gradient(135deg,#8a7a70,#2a2624,#6b5d56)"><div class="play"></div></div>
  <h3>Sed ut perspiciatis unde omnis iste natus</h3>
  <div class="author">Author: Dana Whitlow</div>
  <div class="desc">Sed ut perspiciatis unde omnis iste natus error sit voluptatem accus-antium doloremque laudantium, totam rem aperiam, ipsa quae.</div>
  <div class="more">More &gt;&gt;</div>
  <div class="share" style="left:252px"><b>Like</b><em>20</em></div>
  <div class="share" style="left:308px"><b>Share</b><em>20</em></div>
  <div class="share" style="left:387px"><b>+1</b><em>20</em></div>
</div>

<h2 class="abs heading section-title" style="left:602px;top:470px">Collaborative Video</h2>
<div class="abs video" role="img" aria-label="Film crew with camera and boom microphone shooting on a snowy shore"></div>
<div class="abs video-play"></div>
<div class="abs video-bar"><i></i></div>
<p class="abs body-text" style="left:603px;top:630px;width:212px;text-align:justify">Sed ut perspiciatis unde omnis iste natus error sit voluptatem accusantium doloremque laudantium, totam rem aperiam, eaque ipsa quae ab illo inventore</p>
<div class="abs btn-dark" style="left:760px;top:680px;width:64px;height:26px;line-height:26px;font-size:12px">More</div>

<div class="abs contact-box"></div>
<div class="abs contact-icon"></div>
<h2 class="abs heading" style="left:658px;top:738px;font-size:18px;text-transform:uppercase">Quick Contact</h2>
<div class="abs field" style="top:780px">Name</div>
<div class="abs field" style="top:813px">E-mail</div>
<div class="abs field" style="top:846px">Phone Number</div>
<div class="abs field" style="top:878px">Enquiry</div>
<div class="abs field" style="top:910px;height:44px;padding-top:16px">Details</div>
<div class="abs btn-orange submit">SUBMIT</div>

<!-- footer -->
<footer class="abs footer"></footer>
<div class="abs footer-title">Sign Up to Stay in Touch</div>
<p class="abs footer-text">Please enter your email address below to sign up for our mailing list.</p>
<div class="abs email-input">your email address here..</div>
<div class="abs subscribe">Subscribe ›</div>
<div class="footer-links">
  <a style="left:410px;top:1102px">Home</a>
  <a style="left:410px;top:1121px">Collaborate</a>
  <a style="left:410px;top:1140px">About us</a>
  <a style="left:410px;top:1159px">Contact us</a>
  <a style="left:510px;top:1102px">Privacy Policy</a>
  <a style="left:510px;top:1121px">Terms of Use</a>
  <a style="left:510px;top:1140px">Disclaimer</a>
  <a style="left:510px;top:1159px">Legal Notice</a>
</div>
<div class="abs social" style="left:678px;background:#3b5a9a"></div>
<div class="abs social" style="left:709px;background:#2aa3d8"></div>
<div class="abs social" style="left:740px;background:#3a3a3a"></div>
<div class="abs social" style="left:771px;background:#f29a1d"></div>
<div class="abs social" style="left:802px;background:#c4221c"></div>
<div class="abs social" style="left:834px;background:#7b8a98"></div>
<div class="abs copyright">© 2013 ClipNestra, All Rights Reserved<br>x2</div>

</body>
</html>
```